Website Home Page Re-Design for a Media Company producing Catholic Bible studies on CD/DVD/MP3

UPDATED BRIEF AS OF 12/28/15:

I have been in touch our rep at ArtHive and we are going to extend this design starting on January 9. There were a couple of designs that came out ok -- I could do the tweaking on my end with the body and footer in psd -- but for every single layout the hero section is lacking. So, I guess the main thing that would create a winner is can you create an amazing hero section. I updated the brief once already truncating the focus of design elements -- I am truncating it again here to have you focus on just 1 design element -- who can create the best hero section. Something better has to be possible. I greatly appreciate your attention to this element.

UPDATED BRIEF AS OF 12/21/15:

Ladies and Gentlemen,

Thus far none of the submitted layouts fit the bill (issues being a combination of layouts, design elements, and a lot of samples with too many competing vibrant colors, etc.). So, I just finished putting together an updated template on my own (attached as updated-template.png). I am hoping that now that the layout and color scheme are firmed up (with the exceptions mentioned below), your more focused attention on the following elements will bring about a better result. For, now you are playing/manipulating just elements and not also an overall layout. Please use the bones of this updated template and focus your attention on the following while not adjusting anything not mentioned below:

Starting from the top down:

(1) I'm open to the top section with the logo/need assistance/cart icon/ etc. being manipulated around to make the Sign in and Create account links more noticeable whilst not looking crowded or forced. Not sure if things can go on different lines/different colors implemented, etc. -- that's for you to tinker with if you so choose. Keep the colors of the "Need Assistance" that turquoise blue and the phone and email icons that same orange.

(2) Still open to a better hero section. Found this to be the most disappointing part of the templates submitted thus far. I think rather than slapping images up there on a background that looks like a circus, if some real intricate time was put on making some of the CD's look very nice would help -- how to assemble them and incorporate the tag line is up to you.

(3) For the "Most Popular" and "New Releases" section, if something jumps out at you as far as how to layout the CD images that will populate this section better, I'm open. For instance, would a lighter gray background box work well behind the CD images? Would eliminating the thinly outlined rectangles around the cd images look better? Would assembling them not just in one row horizontally look better, etc.? Keep the titles and those horizontal lines on either sides of the category section the same -- but the layout of the cd images that will populate these sections are open to be modified. Keep in mind NOT TO CROWD THIS AREA -- some templates submitted just looked a mess with not enough white space, making it look very crammed and lacking distinct sections for the eye to be drawn to -- having the effect of "where do I look"?

(4) I need 3 well-designed iconic images for the Blog, Rewards Program, and Chatterly links in the gray rectangular box near the bottom. From top to bottom, the three icons combined (in total height) should be the height of the entire still frame that is situated to the left. Keep in mind, once again, space between them -- they should not looked crammed. FYI, the "Veriday Media Blog" logo as you see on our blog (veridaymediablog.com) should be a part of whatever icon you end up using.

Thank you.

INITIAL BRIEF:

1 PAGE ONLY
I am looking for a re-design of our home page at store.veridaymedia.com -- you can see our current layout there. Our e-commerce store is hosted on ShopLoom.com.

I am uploading a screen shot here of what CONTENT I would like to see on our home page, but obviously it needs to be laid out with a much more professional and polished look to -- not using the layout I currently have -- want someone who really knows what they're doing to create a really polished presentation of the CONTENT. Please pay close attention to the following considerations:

(1) As far as colors, it needs to flow well with the other pages of the website, as those will not be changes (i.e., the category pages and the product pages).

(2) I've laid out the elements in the attached design in somewhat order of importance:

(A) Visitors should see the Catch title of "Grasp the Scriptures As Never Until Now" (though this is subject to modify -- wording may be different) at the top somewhere as an eye catcher (would probably be wise to have some type of graphic like our cd covers as I have them in the screen shot, but this is definitely where your artistic talents of placement and manipulation if graphics must take over). I like the look of the cd sets in the top banner in the attached screen shot inasmuch as they look like they're stepping out of the rectangle/hero section-- obviously you can use whatever image(s) you deem appropriate and can include or exclude this design aspect -- just throwing that out there, but don't think it's mandatory if it doesn't work with the overall design.

(B) Then our most popular Bible studies section which will be populated by automated settings on the back end of shoploom.

(C) Then our Join our email list option

(C.i.) I don't have it in the attached screen shot but we MIGHT end up doing a "Who Are We Video?" I do not know if it is possible to create the page layout such that there is room to add the image of the video still frame at some point in the future. If not just assume no video at this point.

(D) The Latest Releases is beneath the join our email list section merely because I thought there needed to be a break between having two rows of CD's merely differentiated by the title of each row (Most Popular Bible Studies vs. Latest Releases).

(E) Next is something graphically eye catching for our Blog, Chatterly and Rewards Program. Again, I just threw those images together -- not very polished or, in my estimation, very attractive -- your abilities must reign here again.

(F) Then there are what I'd call "secondary" links in the bottom horizontal black bar in the attached screen shot that are currently right beneath the bottom black bar on our current store page (e.g., Home, Services, About Us and so on). Those should be present, but obviously can be laid out in whatever design layout you envision.

(G) The Safeknot, Payment Options, and "All Prices..." need to be present at the bottom too.

(H) Just noticed this -- the Search Bar obviously needs to be present as well in a noticeable way near the "Primary" links.

Again, these are just in order of importance for the most part -- they don't have to go in a perfectly lined up vertical order from top to bottom, but the eye should be drawn to the elements in roughly that order.

(2) We are looking for a clean, "elegant" home page that incorporates the elements in the attached screen shot mentioned above and doesn't look cluttered or busy.

I like the black gradient of the horizontal bars across the top and bottom in conjunction with the flesh-like gradient color of the top rectangle box/hero image -- that contrast, along with a good bit of white space works well, though I'm certainly not opposed to other color schemes -- but it has to be consonant with the other category and product pages on the website pages -- if you re-create the top section and bottom section such that the other category and product pages top and bottom sections need to be modified, that is fine if it means a much better designed home page. Not looking for a super tall page either, but it obviously will need to be taller than it currently stands at store.veridaymedia.com given what we're adding to it.

(3) I don't know if there is a way to make the "Sign In" and "Create Account" more prominent at the top (or elsewhere in the design) - different fonts or fonts + icons, etc.? I think, most probably, Sign in and Create Account need to go first when read from left to right if it stayed in its current position. But, having said that, I'm not opposed to modifying the entire top section either (where our logo and the cart button currently is) if that works better with a winning design.

(4) Obviously we are eliminating the carousel of images -- only one "hero" image.

(5) Any Fonts should be clean and easy to read.

Other comments about our company:

(6) Our target audience is 25-80 year old people (yes, a broad spectrum, but I can at least say our primary audience is not teenage).

(7) Our company is dedicated to providing Catholic Bible studies on CD, DVD, and MP3.

(8) The reason why we are trying to change up the design is to try to make it more explicit what we have to offer in the first 5 seconds for those who land on our home page and do not know much about us. Trying to make it very focused on the products we offer with more image/iconic based sections of content -- e.g., as opposed to just having the text link for cd's, the blog, or the join our email list in the bottom black horizontal bar, we are dedicating a small iconic section to each of those categories.

Requirements
Must have
• Attached is our logo in a png format with both white background and transparent as well as in black and white and in color. You can use the text "Veriday Media" in the logo as found in the png's attached below or shifted over to the right as found at Store.veridaymedia.com.
Nice to have
• I've attached some layouts here that I like -- obviously would want some distinct layouts, but this hopefully relays the design-type, keeping in mind the comments I've made above in the project description.

```html
<!DOCTYPE html>
<html lang="en">
<head>
<meta charset="utf-8">
<title>Veriday Media – Home</title>
<link rel="stylesheet" href="https://fonts.googleapis.com/css2?family=Open+Sans:wght@400;600;700&family=Arimo:wght@400;700&display=swap">
<style>
:root{
  --navy:#0d2a5c;
  --navy-btn:#10295b;
  --red:#d3212a;
  --price:#c8141c;
  --yellow:#f5b800;
  --text:#222;
  --line:#e2e2e2;
  --star:#f2b50f;
  --rule:#3d5a8c;
}
*{box-sizing:border-box;margin:0;padding:0}
html,body{width:769px;height:1200px;overflow:hidden;background:#fff}
body{position:relative;font-family:"Arimo",Arial,sans-serif;color:var(--text);font-size:8px}
.abs{position:absolute}
a{color:inherit;text-decoration:none}

/* header */
.top-left{left:100px;top:25px;line-height:17px;font-size:8px}
.top-left .phone{margin-left:24px}
.brand{left:350px;top:12px;width:70px;text-align:center}
.brand .mark{display:block;width:28px;height:28px;margin:0 auto 6px;background:var(--navy);border-radius:2px}
.brand .name{font-family:"Open Sans",sans-serif;font-weight:700;font-size:8.5px;color:var(--navy);line-height:10px;letter-spacing:.3px}
.top-right{left:474px;top:24px;font-size:7.5px;line-height:18px}
.top-right .sep{border-left:1px solid #999;margin:0 5px}
.cart{left:622px;top:40px}
.cart-total{left:650px;top:44px;font-size:11px;color:var(--navy);font-weight:700}

/* nav */
.nav{left:0;top:78px;width:769px;height:33px;background:linear-gradient(#3a3a3a,#262626)}
.nav ul{list-style:none;display:flex;height:33px;padding-left:95px}
.nav li{color:#fff;font-weight:700;font-size:9px;line-height:33px;padding:0 3px}
.nav li.active{background:var(--yellow);color:#222;padding:0 8px;margin-right:2px}
.search{left:562px;top:84px;width:115px;height:21px;background:#fff;border-radius:11px;font-size:8px;color:#999;padding:5px 8px;font-style:italic}
.search svg{position:absolute;right:8px;top:5px}

/* hero */
.hero{left:0;top:111px;width:769px;height:247px;
  background:
    radial-gradient(ellipse 170px 230px at 640px 110px,rgba(150,108,58,.85),rgba(160,120,70,.45) 55%,rgba(160,120,70,0) 100%),
    radial-gradient(ellipse 260px 160px at 560px 60px,rgba(255,255,255,.95),rgba(255,255,255,0) 70%),
    radial-gradient(ellipse 220px 90px at 200px 90px,rgba(255,255,255,.55),rgba(255,255,255,0) 80%),
    radial-gradient(ellipse 300px 80px at 260px 230px,rgba(255,255,255,.6),rgba(255,255,255,0) 80%),
    linear-gradient(180deg,#3f7fc0 0%,#7fb0dd 55%,#cfe2f2 100%)}
.hero-art{left:114px;top:166px;width:220px;height:128px;
  background:linear-gradient(100deg,#c08a3a 0%,#8a3a22 25%,#2c2a28 50%,#d8c283 75%,#3b3a36 100%);
  border-radius:3px;box-shadow:4px 6px 10px rgba(0,0,0,.3);
  transform:skewY(-2deg)}
.hero-caption{left:93px;top:323px;width:588px;height:35px;background:rgba(255,255,255,.72)}
.hero-caption h1{position:absolute;left:8px;top:7px;font-family:"Open Sans",sans-serif;font-weight:400;font-size:16px;color:#222}
.btn-pill{position:absolute;left:495px;top:8px;width:78px;height:21px;border-radius:11px;background:var(--navy);color:#fff;font-weight:700;font-size:8.5px;line-height:21px;text-align:center}
.hero-rule{left:0;top:358px;width:769px;height:3px;background:var(--navy)}

/* sections */
.section-title{left:93px;width:588px;text-align:center;font-family:"Open Sans",sans-serif;font-weight:600;font-size:12.5px;color:#111}
.section-rule{left:93px;width:588px;height:3px;background:var(--rule)}
.card-img{width:125px;height:125px;border:1px solid #ddd;background:#fff}
.card-img.hl{background:#eee}
.cover{position:absolute;left:22px;top:12px;width:80px;height:84px;border-radius:2px;box-shadow:2px 3px 5px rgba(0,0,0,.25)}
.stars{position:absolute;left:0;width:100%;bottom:6px;text-align:center;color:var(--star);font-size:11px;letter-spacing:1px}
.card-title{font-size:8px;color:#111;white-space:nowrap;width:128px;overflow:hidden}
.card-title.hl{color:var(--price)}
.price{font-family:"Open Sans",sans-serif;font-size:13px;font-weight:600;color:var(--price)}
.reviews{font-size:7px;font-style:italic;color:#333}
.buy{width:125px;height:20px;background:var(--navy-btn);color:#fff;font-size:9px;text-align:center;line-height:20px}
.buy.hl{background:var(--price)}
.divider{width:1px;background:var(--line)}
.arrow{width:26px;height:26px}

/* social band */
.social{left:93px;top:654px;width:588px;height:78px;background:var(--navy)}
.social-box{top:13px;height:51px;background:#fff;border-radius:2px;display:flex;align-items:center;font-size:8.5px;font-weight:700;color:#111}
.social-box .ico{width:32px;height:32px;border-radius:5px;margin:0 10px 0 17px}
.social-box .label{font-size:12px;font-weight:700;color:var(--navy);margin:0 8px 0 10px}

/* signup */
.signup{left:93px;top:1030px;width:588px;height:75px;background:var(--red);border-radius:3px}
.signup h2{position:absolute;left:15px;top:17px;color:#fff;font-family:"Open Sans",sans-serif;font-weight:700;font-size:16.5px;line-height:19px}
.signup h2 small{font-size:13.5px;font-weight:600}
.field{position:absolute;top:27px;height:26px;background:#fff;border-radius:13px;font-size:8px;font-style:italic;color:#999;padding:8px 10px}
.field-go{position:absolute;right:0;top:0;width:34px;height:26px;background:var(--navy);border-radius:13px;color:#fff;font-size:16px;line-height:24px;text-align:center;font-style:normal}

/* footer */
.footer-links{left:0;top:1131px;width:769px;display:flex;justify-content:center;font-size:9px;color:#111}
.footer-links span{padding:0 6px;border-left:1px solid #999}
.footer-links span:first-child{border-left:0}
.bottom{left:0;top:1163px;width:769px;height:37px;background:#333;color:#fff;font-size:7.5px}
.bottom .copy{position:absolute;left:96px;top:15px}
.bottom .copy b{margin:0 6px}
.bottom .accept{position:absolute;left:479px;top:15px}
.pay{position:absolute;top:12px;width:22px;height:14px;background:#fff;border-radius:2px;font-size:5px;color:#222;text-align:center;line-height:14px;font-weight:700}
.seal{position:absolute;left:645px;top:12px;width:27px;height:14px;background:#fff;border-radius:2px}
</style>
</head>
<body>

<!-- header -->
<div class="abs top-left">
  <div>NEED ASSISTANCE?<span class="phone">(555) 014 2736</span></div>
  <div>Check out&nbsp; / &nbsp;Log in&nbsp; / &nbsp;Register&nbsp; / &nbsp;Contact</div>
</div>
<div class="abs brand"><span class="mark"></span><span class="name">VERIDAY<br>MEDIA</span></div>
<div class="abs top-right">
  <div>Gift Certificates<span class="sep"></span>Wishlist<span class="sep"></span>Sign In<span class="sep"></span>Create Account</div>
  <div>E-mail Us &nbsp;&nbsp;&nbsp;&nbsp; My wishlist ( 0 ) / USD</div>
</div>
<svg class="abs cart" width="24" height="20" viewBox="0 0 24 20" aria-hidden="true">
  <path d="M2 6h3l3 8h10l2-6H7" fill="none" stroke="#777" stroke-width="1.5"/>
  <circle cx="9" cy="17" r="1.5" fill="#777"/><circle cx="17" cy="17" r="1.5" fill="#777"/>
  <circle cx="20" cy="4" r="4" fill="#d3212a"/><text x="20" y="6" font-size="5" fill="#fff" text-anchor="middle">0</text>
</svg>
<div class="abs cart-total">$0.00</div>

<!-- nav -->
<nav class="abs nav">
  <ul>
    <li class="active">SPEAKER</li><li>CD</li><li>DVD</li><li>MP3</li><li>CLASS</li><li>BOOK</li><li>CONFERENCE</li><li>CATEOGY</li><li>BLOG</li><li>REWARDS PROGRAM</li>
  </ul>
</nav>
<div class="abs search">Search
  <svg width="11" height="11" viewBox="0 0 11 11" aria-hidden="true"><circle cx="4.5" cy="4.5" r="3.3" fill="none" stroke="#999" stroke-width="1.5"/><path d="M7 7l3 3" stroke="#999" stroke-width="1.5"/></svg>
</div>

<!-- hero -->
<section class="abs hero" role="img" aria-label="Bright blue sky with white clouds and sunburst, a large weathered wooden cross rising on the right"></section>
<div class="abs hero-art" role="img" aria-label="Fanned stack of four Bible study CD set boxes"></div>
<div class="abs hero-caption">
  <h1>Grasp the Scriptures As Never Until Now</h1>
  <a class="btn-pill">SEE DETAILS</a>
</div>
<div class="abs hero-rule"></div>

<!-- most popular -->
<h2 class="abs section-title" style="top:385px">MOST POPULAR BIBLE STUDIES</h2>
<div class="abs section-rule" style="top:406px"></div>

<div class="abs divider" style="left:237px;top:425px;height:207px"></div>
<div class="abs divider" style="left:387px;top:425px;height:207px"></div>
<div class="abs divider" style="left:537px;top:425px;height:207px"></div>

<div class="abs card-img" style="left:102px;top:432px"><div class="cover" role="img" aria-label="CD set cover: The Divine Bridegroom" style="background:linear-gradient(135deg,#8a1c14,#d88a3a)"></div><div class="stars">★★★★★</div></div>
<div class="abs card-img hl" style="left:249px;top:432px"><div class="cover" role="img" aria-label="CD set cover: The Seven Signs of the Lamb" style="background:linear-gradient(135deg,#8a2a20,#d9b36a)"></div><div class="stars">★★★★★</div></div>
<div class="abs card-img" style="left:400px;top:432px"><div class="cover" role="img" aria-label="CD set cover: A Bible Guide to the Liturgy" style="background:linear-gradient(135deg,#b04a1a,#e3a04a)"></div><div class="stars">★★★★★</div></div>
<div class="abs card-img" style="left:549px;top:432px"><div class="cover" role="img" aria-label="CD set cover: A Biblical Journey to Zion" style="background:linear-gradient(135deg,#7a1c1c,#efe3b8)"></div><div class="stars">★★★★★</div></div>

<div class="abs card-title" style="left:102px;top:569px">THE DIVINE BRIDEGROOM</div>
<div class="abs card-title hl" style="left:249px;top:569px">THE SEVEN SIGNS OF THE LAMB</div>
<div class="abs card-title" style="left:400px;top:569px">A BIBLE GUIDE TO THE LITURGY</div>
<div class="abs card-title" style="left:549px;top:569px">A BIBLICAL JOURNEY TO ZION</div>

<div class="abs price" style="left:102px;top:581px">$ 200.00</div><div class="abs reviews" style="left:185px;top:586px">- 5 Reviews</div>
<div class="abs price" style="left:249px;top:581px">$ 270.00</div><div class="abs reviews" style="left:332px;top:586px">- 7 Reviews</div>
<div class="abs price" style="left:400px;top:581px">$ 270.00</div><div class="abs reviews" style="left:483px;top:586px">- 3 Reviews</div>
<div class="abs price" style="left:549px;top:581px">$ 270.00</div><div class="abs reviews" style="left:632px;top:586px">- 8 Reviews</div>

<a class="abs buy" style="left:102px;top:604px">BUY NOW</a>
<a class="abs buy hl" style="left:249px;top:604px">BUY NOW</a>
<a class="abs buy" style="left:400px;top:604px">BUY NOW</a>
<a class="abs buy" style="left:549px;top:604px">BUY NOW</a>

<svg class="abs arrow" style="left:59px;top:598px" viewBox="0 0 26 26" aria-label="Previous"><circle cx="13" cy="13" r="12" fill="#fff" stroke="#bbb" stroke-width="2"/><path d="M15 8l-5 5 5 5" fill="none" stroke="#bbb" stroke-width="2"/></svg>
<svg class="abs arrow" style="left:687px;top:508px" viewBox="0 0 26 26" aria-label="Next"><circle cx="13" cy="13" r="12" fill="#fff" stroke="#bbb" stroke-width="2"/><path d="M11 8l5 5-5 5" fill="none" stroke="#bbb" stroke-width="2"/></svg>

<!-- social band -->
<section class="abs social">
  <div class="abs social-box" style="left:20px;width:157px"><span class="ico" style="background:#f57d00"></span>FOLLOW OUR BLOG</div>
  <div class="abs social-box" style="left:198px;width:192px"><span class="label">Chatterly</span>CONNECT WITH US</div>
  <div class="abs social-box" style="left:410px;width:157px"><span class="ico" style="background:#2b8fd6"></span>GET REWARDED</div>
</section>

<!-- latest releases -->
<h2 class="abs section-title" style="top:759px">LATEST RELEASES</h2>
<div class="abs section-rule" style="top:780px"></div>

<div class="abs divider" style="left:237px;top:795px;height:207px"></div>
<div class="abs divider" style="left:387px;top:795px;height:207px"></div>
<div class="abs divider" style="left:537px;top:795px;height:207px"></div>

<div class="abs card-img" style="left:102px;top:801px"><div class="cover" role="img" aria-label="CD set cover: The Divine Bridegroom" style="background:linear-gradient(135deg,#8a1c14,#d88a3a)"></div><div class="stars">★★★★★</div></div>
<div class="abs card-img" style="left:249px;top:801px"><div class="cover" role="img" aria-label="CD set cover: The Seven Signs of the Lamb" style="background:linear-gradient(135deg,#8a2a20,#d9b36a)"></div><div class="stars">★★★★★</div></div>
<div class="abs card-img" style="left:400px;top:801px"><div class="cover" role="img" aria-label="CD set cover: A Bible Guide to the Liturgy" style="background:linear-gradient(135deg,#b04a1a,#e3a04a)"></div><div class="stars">★★★★★</div></div>
<div class="abs card-img" style="left:549px;top:801px"><div class="cover" role="img" aria-label="CD set cover: A Biblical Journey to Zion" style="background:linear-gradient(135deg,#7a1c1c,#efe3b8)"></div><div class="stars">★★★★★</div></div>

<div class="abs card-title" style="left:102px;top:940px">THE DIVINE BRIDEGROOM</div>
<div class="abs card-title" style="left:249px;top:940px">THE SEVEN SIGNS OF THE LAMB</div>
<div class="abs card-title" style="left:400px;top:940px">A BIBLE GUIDE TO THE LITURGY</div>
<div class="abs card-title" style="left:549px;top:940px">A BIBLICAL JOURNEY TO ZION</div>

<div class="abs price" style="left:102px;top:953px">$ 200.00</div><div class="abs reviews" style="left:185px;top:958px">- 5 Reviews</div>
<div class="abs price" style="left:249px;top:953px">$ 270.00</div><div class="abs reviews" style="left:332px;top:958px">- 7 Reviews</div>
<div class="abs price" style="left:400px;top:953px">$ 270.00</div><div class="abs reviews" style="left:483px;top:958px">- 3 Reviews</div>
<div class="abs price" style="left:549px;top:953px">$ 270.00</div><div class="abs reviews" style="left:632px;top:958px">- 8 Reviews</div>

<a class="abs buy" style="left:102px;top:976px">BUY NOW</a>
<a class="abs buy" style="left:249px;top:976px">BUY NOW</a>
<a class="abs buy" style="left:400px;top:976px">BUY NOW</a>
<a class="abs buy" style="left:549px;top:976px">BUY NOW</a>

<svg class="abs arrow" style="left:59px;top:957px" viewBox="0 0 26 26" aria-label="Previous"><circle cx="13" cy="13" r="12" fill="#fff" stroke="#bbb" stroke-width="2"/><path d="M15 8l-5 5 5 5" fill="none" stroke="#bbb" stroke-width="2"/></svg>
<svg class="abs arrow" style="left:687px;top:867px" viewBox="0 0 26 26" aria-label="Next"><circle cx="13" cy="13" r="12" fill="#fff" stroke="#bbb" stroke-width="2"/><path d="M11 8l5 5-5 5" fill="none" stroke="#bbb" stroke-width="2"/></svg>

<!-- signup -->
<section class="abs signup">
  <h2>Join over 10,000 Catholics<br><small>and get a free Elden Marsh MP3</small></h2>
  <div class="field" style="left:248px;width:125px">First name</div>
  <div class="field" style="left:380px;width:195px">Enter here your email adress<span class="field-go">+</span></div>
</section>

<!-- footer -->
<nav class="abs footer-links">
  <span>HOME</span><span>SERVICES</span><span>ABOUT US</span><span>INVITE A SPEAKER</span><span>EVENTS</span><span>ORDER FORMS</span><span>TERMS &amp; CONDITIONS</span><span>CONTACT US</span>
</nav>
<footer class="abs bottom">
  <div class="copy">© 2015 |<b>VERIDAY MEDIA</b>|&nbsp;&nbsp; All rights reserved.</div>
  <div class="accept">We accept :</div>
  <div class="pay" style="left:526px">PayWell</div>
  <div class="pay" style="left:553px">Nova</div>
  <div class="pay" style="left:580px">Circlo</div>
  <div class="pay" style="left:607px">Vexa</div>
  <div class="seal" role="img" aria-label="Safeknot security seal"></div>
</footer>

</body>
</html>
```